Professional/modern business card design for construction company

We need a new business card design, double sided keeping it modern, sleek, professional and simple. We are an earthmoving business but do not want any pictures of machinery. I would like one side to have the logo and the other to have all the information, keeping with the colors in our logo. The business card will need to be able to be customised so we can use it for several different managers., we would also like to be able to use the design to apply it to other stationary ie. letterheads, notebooks etc. We do not really have a tag line but we could put on there that we specialise in - Agriculture, Civil Construction and Mining.

Contact Information for Business Card

Brolga Ridge Excavations Pty Ltd
ABN 58 402 937 615
82 Gumleaf Creek Road, Moree NSW 2400

Harold Benton
Managing Director
P 0418 639 204
E haroldbenton@brolgaridgeexc.com.au

Font styles to use
Serif
Sans Serif

Requirements
Nice to have
• I have attached some examples of ideas.
Should not have
• images of machinery

```html
<!DOCTYPE html>
<html lang="en">
<head>
<meta charset="utf-8">
<title>Brolga Ridge Excavations – Business Card</title>
<link href="https://fonts.googleapis.com/css2?family=Poppins:wght@400;500;600;700&family=Raleway:wght@600&display=swap" rel="stylesheet">
<style>
  :root {
    --bg: #1f1d1d;
    --card: #ffffff;
    --ink: #4a4a4a;
    --ink-soft: #555555;
    --orange: #f7931e;
    --hatch: #b9b9b9;
    --rule: #8a8a8a;
  }
  * { margin: 0; padding: 0; box-sizing: border-box; }
  html, body { width: 1200px; height: 1200px; overflow: hidden; background: var(--bg); }
  body { position: relative; font-family: 'Poppins', sans-serif; }

  .card {
    position: absolute;
    left: 257px;
    width: 686px;
    height: 392px;
    background: var(--card);
  }
  .card--front { top: 176px; }
  .card--back { top: 632px; }

  .hatch-frame {
    position: absolute; inset: 0;
    background: repeating-linear-gradient(45deg, var(--hatch) 0 1px, #fff 1px 4px);
  }
  .hatch-frame::after {
    content: ""; position: absolute;
    inset: 14px; background: var(--card);
  }
  .hatch-strip {
    position: absolute; left: 0; right: 0; bottom: 0; height: 12px;
    background: repeating-linear-gradient(45deg, var(--hatch) 0 1px, #fff 1px 4px);
  }

  .brand {
    position: absolute; left: 62px; top: 150px; width: 240px;
    display: flex; align-items: center; gap: 12px;
  }
  .brand__mark { width: 22px; height: 22px; background: var(--orange); flex: none; }
  .brand__name {
    color: var(--ink); font-weight: 600; font-size: 22px; line-height: 1.15;
    letter-spacing: 0.5px; text-transform: uppercase;
  }

  .divider {
    position: absolute; left: 324px; top: 89px; width: 1px; height: 208px;
    background: var(--rule);
  }

  .details { position: absolute; left: 355px; top: 88px; color: var(--ink-soft); }
  .details__name { color: var(--orange); font-weight: 700; font-size: 25px; line-height: 1.1; text-transform: uppercase; }
  .details__role { font-size: 16px; line-height: 1.3; margin: 2px 0 10px 3px; color: var(--ink); }
  .details__block { font-size: 15.5px; line-height: 19.5px; }
  .details__block + .details__block { margin-top: 10px; }
  .details__block--tight { margin-top: 6px !important; }

  .tagline {
    position: absolute; left: 0; right: 0; top: 170px;
    text-align: center; font-family: 'Raleway', sans-serif; font-weight: 600;
    font-size: 17px; line-height: 21px; color: var(--ink);
  }
</style>
</head>
<body>
  <section class="card card--front">
    <div class="hatch-frame"></div>
    <div class="brand">
      <span class="brand__mark"></span>
      <span class="brand__name">Brolga Ridge Excavations Pty Ltd</span>
    </div>
    <div class="divider"></div>
    <div class="details">
      <h1 class="details__name">Harold Benton</h1>
      <p class="details__role">Managing Director</p>
      <p class="details__block">Brolga Ridge Excavations Pty Ltd<br>82 Gumleaf Creek Road<br>Moree NSW 2400</p>
      <p class="details__block">ABN 58 402 937 615</p>
      <p class="details__block details__block--tight">0418 639 204<br>haroldbenton@brolgaridgeexc.com.au<br>www.brolgaridgeexc.com.au</p>
    </div>
  </section>

  <section class="card card--back">
    <p class="tagline">We specialise in<br>Agriculture, Civil Construction &amp; Mining.</p>
    <div class="hatch-strip"></div>
  </section>
</body>
</html>
```